Brindle Chill Supplies Stationery Design

Stationery Design

Thank you to all those who have submitted the logos. We have selected the logo for our new identity and we are now looking for stationery ideas.

The attached logo must be used in all stationery designs.

We require the following items of stationery:

1. Business Cards for 10 employees – Double Sided – All the card will have the same address:

7 – 31 Marrowby Lane, Kingston Upon Thames, Surrey, KT4 9QX, United Kingdom

Office phone number: +44 (0)208 613 7742

Freephone: 0800 129 4837

Fax: +44 (0)20 8731 2964

Website: www.brindlechill.example

The names on the cards and mobile numbers – will be given on selection of final design.

A few of the cards will have different emails but 5/6 card will have the same email address.

2. Letterhead A4 – same contact details as above – email address to be used info@brindlechill.example

3. Compliments Slip – same details as no.2

4. Envelope designs – with just the address, Freephone and Website.

Sizes Required: C4 – 324mm x 229mm – Windows and Regular

DL – 110mm x 220mm – Windows and Regular

5. A4 Ring Binder – Logo at the front and back and side; company name on the front and side of the binder (Brindle Chill Supplies); contact details at the back; same as number 2 above.

The ring binder will have food, drink and hygiene inserts inside and will act as a temporary brochure.

It may help with the design process to know we sell a range of frozen food products including chips, burgers, fish, frozen poultry items, vegetables, ice cream, desserts, bakery products, pies, pasties, onion rings, pizza toppings etc.

We also sell ambient products such as sauces, crisps such as dunmores, chocolates such as Hollensby, Vorelle, Quib etc.

Drinks wise we sell branded products such as zesta tonic, fizmo, lumra, glint, sky hare etc; As well as juices and mineral water.

We also sell hygiene products such as tissue paper, hand towels, and other washroom products, bleaches etc.

Our website doesn’t have the full range of products but gives you a good idea of what we do www.brindlechill.example

Please note we are looking for a classy, slick design so don’t worry about trying to add all the products on the binder design; these have just been given to assist with the design process.

We may add a slogan to the stationery but the final decision on this still has to be taken and the profile will be updated within the next 72 hours.

This project will only last a maximum of 10-14 days, we don’t want to drag it out like the logo so please only submit creative ideas; which have been given thought in terms of design, text and graphics.

Any questions, feel free to ask.

Thank you and we look forward to your designs.

Regards

Torvin Ashcombe

I've uploaded an Adobe Illustrator CS2.ai file, and an EPS file of my new logo so you can get better clarity within your designs for this project

Thanks
Torvin

Hi

We have had various questions in respect of dimensions and budget; we have addressed both issues below by providing dimensions and we will be increasing the budget to $500 as soon as Pixel Bazaar let us know how we can increase; they have already been emailed.

In respect of the dimensions, we have had various answers but here are the most common sizes.

 

There are various sizes of lever arch A4 folders but the most common ones are below:

 

 

• Dimensions width 28.5cm, height 32cm,spine 9cm
• Dimensions (mm)H:315 x W:285
• Dimensions (mm) H:31cm x W:27cm

 

The most common thickness in the UK seems to be 70mm; so can we use this as a guide please.

 

 

Compliment Slip Sizes:

 

• Our Compliment Slips are DL in size. You should design your Compliment Slip to DL dimension but also add a 3mm bleed around each edge.

 

Trim Size – 99mm x 210mm

 

With Bleed – 105mm – 216mm

 

 

Business Cards:

 

Trim Size: 85mm x 55mm

 

With Bleed: 91mm x 61mm

 

 

We have extended the time frame and the budget on this so look forward to new designs.

 

I hope this helps and all the best for Christmas and 2010..

 

Regards

Torvin Ashcombe.

Hi Guys

Another important point to mention as each country has different rules...

In the Uk the postage stamps go in the top right hand corner of the envelope so we will have to have our logo company details etc in either the top left or the bottom of the envelope.

Also all envelopes must have at the back our return address:

Return Address:

Brindle Chill Supplies Ltd
7 - 31 Marrowby Lane
Kingston Upon Thames
Surrey
KT4 9QX

So we could even have the business logo, name and website address at the front and the address at the back.

Regards

Torvin

```html
<!DOCTYPE html>
<html lang="en">
<head>
<meta charset="utf-8">
<title>Brindle Chill Supplies – Stationery Set</title>
<link rel="stylesheet" href="https://fonts.googleapis.com/css2?family=Exo+2:wght@400;500;600&family=Signika:wght@500;600&display=swap">
<style>
:root{
  --board:#4d4540;
  --paper:#ffffff;
  --ink:#1b1b1f;
  --grey:#7a7a7a;
  --red:#a5212c;
  --red-soft:#e0a4ab;
  --navy:#2c2a6e;
  --navy-soft:#a8a6c8;
  --sky:#dbe9f7;
  --tag:#f7a65a;
}
*{margin:0;padding:0;box-sizing:border-box}
html,body{width:1200px;height:978px;overflow:hidden;background:var(--board)}
body{position:relative;font-family:"Exo 2",sans-serif;color:var(--ink)}
.abs{position:absolute}
.sheet{position:absolute;background:var(--paper);box-shadow:2px 3px 6px rgba(0,0,0,.35);overflow:hidden}
.swoosh{position:absolute;inset:0;width:100%;height:100%}
.tag{position:absolute;background:var(--tag);font-family:"Signika",sans-serif;font-weight:600;font-size:14px;letter-spacing:2.5px;color:#2a1e14;display:flex;align-items:center;padding-left:14px;white-space:nowrap;overflow:hidden}

.brand{position:absolute;display:flex;align-items:center;gap:6px;font-family:"Exo 2",sans-serif;font-weight:600;color:var(--ink);white-space:nowrap;z-index:2}
.brand i{display:block;border-radius:50%;background:var(--red);flex:none}

.contact{position:absolute;font-size:7px;line-height:1.35;color:var(--grey);white-space:nowrap;z-index:2}

.binder{left:27px;top:27px;width:998px;height:461px}
.guide{position:absolute;top:0;bottom:0;width:1px;background:#7fd3e0;opacity:.7;z-index:3}
.photo{position:absolute}
.photo.framed{outline:2px solid var(--tag);outline-offset:-2px}
.brochure-title{position:absolute;left:684px;top:30px;font-family:"Signika",sans-serif;font-weight:600;font-size:24px;letter-spacing:3px;color:var(--red);white-space:nowrap;z-index:2}
.spine-title{position:absolute;left:426px;top:266px;width:140px;text-align:center;font-family:"Signika",sans-serif;font-weight:600;font-size:12px;line-height:1.25;letter-spacing:2px;color:var(--red);z-index:2}
.spine-name{position:absolute;left:487px;top:86px;writing-mode:vertical-rl;font-family:"Exo 2",sans-serif;font-weight:600;font-size:14px;color:var(--ink);white-space:nowrap;z-index:2}
.spine-dot{position:absolute;left:473px;top:22px;width:48px;height:48px;border-radius:50%;background:var(--red);z-index:2}
</style>
</head>
<body>

<section class="sheet binder">
  <svg class="swoosh" viewBox="0 0 998 461" preserveAspectRatio="none" aria-hidden="true" style="z-index:1">
    <path d="M0,461 C200,390 380,340 560,330 C760,322 900,380 998,440 L998,461 Z" fill="var(--sky)"/>
    <path d="M426,360 C520,320 620,298 730,300 C860,304 950,360 998,400 L998,432 C940,392 850,340 730,336 C620,334 520,356 426,392 Z" fill="var(--navy)" opacity=".82"/>
    <path d="M0,461 L40,461 C150,420 300,378 470,350 L566,338 L566,318 L470,326 C290,352 130,410 0,452 Z" fill="var(--red)" opacity=".85"/>
  </svg>

  <div class="guide" style="left:425px"></div>
  <div class="guide" style="left:566px"></div>

  <div class="brand" style="left:16px;top:30px;font-size:22px"><i style="width:30px;height:30px"></i>Brindle Chill Supplies</div>
  <div class="abs" style="left:23px;top:84px;font-size:16px;color:var(--grey)">www.brindlechill.example</div>
  <div class="contact" style="left:22px;top:118px;font-size:8px">Office: +44 (0)208 613 7742<br>Freephone: 0800 129 4837<br>Fax: +44 (0)20 8731 2964</div>
  <div class="contact" style="left:22px;top:160px;font-size:8px">7 – 31 Marrowby Lane, Kingston Upon Thames<br>Surrey, KT4 9QX, United Kingdom</div>
  <div class="contact" style="left:22px;top:190px;font-size:8px">info@brindlechill.example</div>

  <div class="spine-dot"></div>
  <div class="spine-name">Brindle Chill Supplies</div>
  <div class="spine-title">PRODUCTS<br>BROCHURE</div>

  <div class="brochure-title">PRODUCTS BROCHURE</div>
  <div class="photo" role="img" aria-label="Glasses of orange juice and red fruit drink" style="left:566px;top:8px;width:103px;height:154px;background:linear-gradient(90deg,#e9b24a,#b8202e)"></div>
  <div class="photo framed" role="img" aria-label="Ice cream cone with sprinkles" style="left:676px;top:79px;width:60px;height:83px;background:linear-gradient(#d9c2b0,#7a4a2e)"></div>
  <div class="photo" role="img" aria-label="Baked cookies" style="left:744px;top:79px;width:126px;height:83px;background:linear-gradient(135deg,#c9a770,#8a6a3c)"></div>
  <div class="photo" role="img" aria-label="Frozen chips" style="left:876px;top:79px;width:122px;height:83px;background:linear-gradient(135deg,#f0a24a,#d9731f)"></div>
  <div class="photo" role="img" aria-label="Fresh vegetables and fruit" style="left:566px;top:170px;width:125px;height:84px;background:linear-gradient(135deg,#8fae4e,#c2402e)"></div>
  <div class="photo" role="img" aria-label="Bar of chocolate" style="left:697px;top:170px;width:126px;height:84px;background:linear-gradient(135deg,#8a5a36,#5a3418)"></div>
  <div class="photo framed" role="img" aria-label="Cooking pot" style="left:830px;top:170px;width:38px;height:39px;background:#e4e4e4"></div>
  <div class="photo framed" role="img" aria-label="Serving pan" style="left:830px;top:213px;width:38px;height:41px;background:#ebebeb"></div>
  <div class="photo" role="img" aria-label="Grilled burgers and sausages" style="left:876px;top:170px;width:122px;height:108px;background:linear-gradient(135deg,#6a3a24,#3a1e12)"></div>
  <div class="photo" role="img" aria-label="Frozen poultry pieces" style="left:566px;top:262px;width:302px;height:66px;background:linear-gradient(90deg,#5e8ab8,#d8c2a4 40%,#cdb898)"></div>
  <div class="photo" role="img" aria-label="Sliced carrots and potatoes" style="left:876px;top:286px;width:122px;height:65px;background:linear-gradient(135deg,#f08a2a,#e8c23a)"></div>

  <div class="brand" style="left:598px;top:380px;font-size:24px;gap:10px"><i style="width:46px;height:46px"></i>Brindle Chill Supplies</div>
</section>
<div class="tag" style="left:222px;top:434px;width:218px;height:40px;z-index:3">BUSINESS CARD Fr/Bk</div>
<div class="tag" style="left:945px;top:434px;width:224px;height:38px;z-index:3">A4 BINDER</div>

<article class="sheet" style="left:223px;top:165px;width:217px;height:123px;z-index:2">
  <div class="abs" style="left:11px;top:10px;font-size:8px;color:var(--red)">FIRST N. LASTNAME</div>
  <div class="contact" style="left:11px;top:23px;font-size:6px">Position<br>flastname@brindlechill.example</div>
  <div class="contact" style="left:11px;top:53px;font-size:5.5px">Office: +44 (0)208 613 7742<br>Freephone: 0800 129 4837<br>Fax: +44 (0)20 8731 2964</div>
  <div class="brand" style="left:96px;top:54px;font-size:8px;gap:4px"><i style="width:15px;height:15px"></i>Brindle Chill Supplies</div>
  <svg class="swoosh" viewBox="0 0 100 100" preserveAspectRatio="none" aria-hidden="true">
    <path d="M0,100 L0,92 C30,72 65,66 100,78 L100,100 Z" fill="var(--sky)"/>
    <path d="M0,96 L0,86 C30,70 60,66 100,72 L100,78 C65,70 35,76 0,96 Z" fill="var(--navy)"/>
    <path d="M0,100 L0,92 C20,80 38,76 55,74 L55,76 C38,80 20,88 6,100 Z" fill="var(--red)"/>
  </svg>
</article>

<article class="sheet" style="left:223px;top:300px;width:217px;height:124px;background:var(--sky);z-index:2">
  <div class="brand" style="left:38px;top:24px;font-size:12px"><i style="width:24px;height:24px"></i>Brindle Chill Supplies</div>
  <div class="abs" style="left:0;right:0;top:75px;text-align:center;font-size:6px;line-height:1.4;color:var(--red)">7 – 31 Marrowby Lane, Kingston Upon Thames<br>Surrey, KT4 9QX, United Kingdom</div>
  <div class="abs" style="left:0;right:0;top:98px;text-align:center;font-size:7px;color:var(--navy)">www.brindlechill.example</div>
</article>

<article class="sheet" style="left:27px;top:509px;width:339px;height:168px">
  <div class="brand" style="left:7px;top:8px;font-size:12px"><i style="width:22px;height:22px"></i>Brindle Chill Supplies</div>
  <div class="contact" style="left:40px;top:38px;font-size:4px;line-height:1.5">7 – 31 Marrowby Lane, Kingston Upon Thames<br>Surrey, KT4 9QX, United Kingdom<br><br>Freephone: 0800 129 4837<br>www.brindlechill.example</div>
  <svg class="swoosh" viewBox="0 0 100 100" preserveAspectRatio="none" aria-hidden="true">
    <path d="M30,100 C50,80 75,72 100,80 L100,100 Z" fill="#eef4fb"/>
    <path d="M28,100 C45,78 68,68 100,72 L100,78 C70,72 48,82 34,100 Z" fill="var(--red-soft)"/>
    <path d="M48,78 C65,66 85,64 100,74 L100,84 C85,70 68,70 52,80 Z" fill="var(--navy-soft)"/>
  </svg>
</article>
<div class="tag" style="left:143px;top:689px;width:223px;height:40px">DL ENVELOPES</div>

<article class="sheet" style="left:55px;top:751px;width:311px;height:146px">
  <div class="abs" style="left:10px;top:12px;font-size:7px;color:var(--grey)">WITH COMPLIMENTS</div>
  <div class="brand" style="left:196px;top:12px;font-size:7.5px;gap:4px"><i style="width:18px;height:18px"></i>Brindle Chill Supplies</div>
  <div class="contact" style="left:236px;top:48px;font-size:5.5px">Office: +44 (0)208 613 7742<br>Freephone: 0800 129 4837<br>Fax: +44 (0)20 8731 2964</div>
  <div class="contact" style="left:236px;top:78px;font-size:5.5px">info@brindlechill.example<br>www.brindlechill.example</div>
  <svg class="swoosh" viewBox="0 0 100 100" preserveAspectRatio="none" aria-hidden="true">
    <path d="M16,100 C45,72 75,66 100,76 L100,100 Z" fill="#e4eef9"/>
    <path d="M14,100 C40,74 65,64 100,70 L100,76 C68,68 44,80 20,100 Z" fill="var(--red-soft)"/>
    <path d="M40,78 C60,64 82,62 100,74 L100,86 C82,70 62,70 45,80 Z" fill="var(--navy-soft)"/>
  </svg>
  <div class="contact" style="left:145px;top:133px;font-size:4px;color:#555">7 – 31 Marrowby Lane, Kingston Upon Thames, Surrey, KT4 9QX, United Kingdom</div>
</article>
<div class="tag" style="left:143px;top:911px;width:223px;height:39px">COMPLIMENTS SLIP</div>

<article class="sheet" style="left:388px;top:509px;width:311px;height:441px">
  <svg class="swoosh" viewBox="0 0 311 441" preserveAspectRatio="none" aria-hidden="true">
    <path d="M0,0 L311,0 L280,0 C230,30 140,50 0,30 Z" fill="#e8f0f9"/>
    <path d="M0,18 C90,50 200,40 275,0 L262,0 C200,30 100,40 0,10 Z" fill="var(--red-soft)"/>
    <path d="M0,22 C80,56 180,54 240,10 L232,8 C170,48 90,46 0,14 Z" fill="var(--navy-soft)"/>
  </svg>
  <div class="contact" style="left:42px;top:10px;font-size:3.5px">www.brindlechill.example<br>info@brindlechill.example</div>
  <div class="contact" style="left:94px;top:10px;font-size:3.5px">Office: +44 (0)208 613 7742<br>Freephone: 0800 129 4837<br>Fax: +44 (0)20 8731 2964</div>
  <div class="brand" style="left:196px;top:34px;font-size:8px;gap:4px"><i style="width:20px;height:20px"></i>Brindle Chill Supplies</div>
  <div class="contact" style="left:166px;top:425px;font-size:3.5px">7 – 31 Marrowby Lane, Kingston Upon Thames, Surrey, KT4 9QX, United Kingdom</div>
</article>
<div class="tag" style="left:722px;top:911px;width:154px;height:39px">LETTERHEAD</div>

<article class="sheet" style="left:722px;top:509px;width:447px;height:315px">
  <div class="brand" style="left:16px;top:12px;font-size:17px"><i style="width:36px;height:36px"></i>Brindle Chill Supplies</div>
  <div class="contact" style="left:61px;top:56px;font-size:5px;line-height:1.5">7 – 31 Marrowby Lane, Kingston Upon Thames<br>Surrey, KT4 9QX, United Kingdom<br><br>Freephone: 0800 129 4837<br>www.brindlechill.example</div>
  <svg class="swoosh" viewBox="0 0 100 100" preserveAspectRatio="none" aria-hidden="true">
    <path d="M32,100 C55,84 78,80 100,86 L100,100 Z" fill="#eef4fb"/>
    <path d="M31,100 C50,84 72,76 100,78 L100,82 C74,80 52,88 36,100 Z" fill="var(--red-soft)"/>
    <path d="M50,84 C66,74 86,74 100,84 L100,92 C86,80 68,79 54,86 Z" fill="var(--navy-soft)"/>
  </svg>
</article>
<div class="tag" style="left:945px;top:836px;width:224px;height:40px">C4 ENVELOPE</div>

</body>
</html>
```